Tidewell Outfitters Mobile RV Repair

We are looking for a logo and business cards for a new start up business. We will be doing Mobile RV Repair.
We are in Texas.
I don't have any designs at this point.

Contact Information for Business Card

Emphasis should be on the “Mobile RV Repair” and not so much the name “Tidewell Outfitters”

Requirements
Nice to have
• I like the Mobile RV Repair to cover most of the backside of the card! Not sure on the colors, would like to see it in a few different colors!

```html
<!DOCTYPE html>
<html lang="en">
<head>
<meta charset="utf-8">
<title>Tidewell Outfitters – Business Cards</title>
<link rel="stylesheet" href="https://fonts.googleapis.com/css2?family=Saira:wght@200;300;600&family=Orbitron:wght@500;600&display=swap">
<style>
  :root {
    --backdrop: #504e4d;
    --card-dark: #232323;
    --orange: #e8712a;
    --orange-deep: #d4611f;
    --white: #f2f2f2;
    --ink: #2b2b2b;
    --strip-light: #e4e4e4;
    --fold: #8a8a8a;
  }
  * { margin: 0; padding: 0; box-sizing: border-box; }
  html, body { width: 1200px; height: 1200px; overflow: hidden; }
  body { background: var(--backdrop); position: relative; font-family: "Saira", sans-serif; }

  .card {
    position: absolute; left: 243px; width: 702px; height: 400px;
    border-radius: 24px; overflow: hidden; background: var(--card-dark);
  }
  .card--front { top: 170px; }
  .card--back { top: 630px; }

  /* Front */
  .phone-band {
    position: absolute; left: 0; top: 0; width: 67px; height: 100%;
    background: var(--orange);
  }
  .phone-band__number {
    position: absolute; left: 50%; top: 50%;
    transform: translate(-50%, -50%) rotate(-90deg);
    font-family: "Orbitron", sans-serif; font-weight: 500;
    font-size: 40px; color: var(--white); white-space: nowrap; letter-spacing: 1px;
  }
  .headline__mobile {
    position: absolute; left: 125px; top: 100px; width: 540px;
    display: flex; justify-content: space-between;
    font-weight: 200; font-size: 64px; color: var(--white); line-height: 1;
  }
  .headline__service {
    position: absolute; left: 122px; top: 172px;
    font-weight: 600; font-size: 120px; line-height: 1; letter-spacing: -2px;
    white-space: nowrap;
  }
  .headline__rv { color: var(--orange); margin-right: 14px; }
  .headline__repair { color: var(--white); }

  /* Back */
  .back__panel {
    position: absolute; left: 0; top: 0; width: 367px; height: 100%;
    background: linear-gradient(160deg, var(--orange) 0%, var(--orange-deep) 100%);
  }
  .brand-box {
    position: absolute; left: 54px; top: 83px; width: 234px; height: 235px;
    background: linear-gradient(180deg, #ffffff, #ececec); border-radius: 16px;
    display: flex; flex-direction: column; align-items: center; justify-content: center; gap: 6px;
    text-align: center;
  }
  .brand-box__mark { width: 16px; height: 16px; background: var(--orange); border-radius: 50%; margin-bottom: 8px; }
  .brand-box__name, .brand-box__tag {
    font-weight: 600; color: var(--ink); line-height: 1.1;
  }
  .brand-box__name { font-size: 22px; }
  .brand-box__tag { font-size: 13px; letter-spacing: 3px; text-transform: uppercase; }

  .name-plate {
    position: absolute; left: 347px; top: 38px; width: 275px; height: 80px;
    background: linear-gradient(180deg, #ffffff, #e6e6e6);
    display: flex; align-items: center; justify-content: center;
    font-family: "Orbitron", sans-serif; font-weight: 600; font-size: 25px;
    color: var(--ink); letter-spacing: 1px;
  }
  .name-plate__fold { position: absolute; left: 347px; top: 118px; }

  .contact-strip {
    position: absolute; left: 347px; top: 294px; width: 39px; height: 106px;
    background: var(--strip-light);
  }
  .contact {
    position: absolute; left: 353px; display: flex; align-items: center; gap: 12px;
    font-family: "Saira", sans-serif; font-weight: 300; font-size: 16px;
    color: var(--white); letter-spacing: 0.5px; white-space: nowrap;
  }
  .contact--phone { top: 314px; }
  .contact--mail { top: 355px; }
  .contact__icon { width: 26px; height: 26px; flex: none; }
</style>
</head>
<body>

<section class="card card--front" aria-label="Business card front">
  <div class="phone-band"><span class="phone-band__number">210-555-0147</span></div>
  <div class="headline__mobile" aria-label="Mobile">
    <span>M</span><span>O</span><span>B</span><span>I</span><span>L</span><span>E</span>
  </div>
  <div class="headline__service"><span class="headline__rv">RV</span><span class="headline__repair">Repair</span></div>
</section>

<section class="card card--back" aria-label="Business card back">
  <div class="back__panel"></div>
  <div class="brand-box">
    <span class="brand-box__mark"></span>
    <span class="brand-box__name">Tidewell Outfitters</span>
    <span class="brand-box__tag">Mobile RV Repair</span>
  </div>

  <div class="name-plate">MARCUS HOLLEN</div>
  <svg class="name-plate__fold" width="20" height="20" viewBox="0 0 20 20" aria-hidden="true">
    <polygon points="0,0 20,0 20,20" fill="var(--fold)"/>
  </svg>

  <div class="contact-strip"></div>
  <div class="contact contact--phone">
    <svg class="contact__icon" viewBox="0 0 26 26" aria-hidden="true">
      <circle cx="13" cy="13" r="12" fill="#3a3a3a"/>
      <path d="M9 7.5c.6-.5 1.4-.4 1.8.2l1.2 1.8c.3.5.2 1.1-.2 1.5l-.8.7c.7 1.5 1.8 2.7 3.3 3.5l.7-.8c.4-.4 1-.5 1.5-.2l1.8 1.2c.6.4.7 1.2.2 1.8l-.9 1c-.6.6-1.5.8-2.3.5-3.5-1.3-6.2-4-7.5-7.5-.3-.8-.1-1.7.5-2.3z" fill="var(--white)"/>
    </svg>
    <span>210-555-0147</span>
  </div>
  <div class="contact contact--mail">
    <svg class="contact__icon" viewBox="0 0 26 26" aria-hidden="true">
      <circle cx="13" cy="13" r="12" fill="#3a3a3a"/>
      <rect x="7" y="8.5" width="12" height="9" rx="1.5" fill="none" stroke="var(--white)" stroke-width="1.6"/>
      <path d="M7.5 9.5 13 14l5.5-4.5" fill="none" stroke="var(--white)" stroke-width="1.6"/>
    </svg>
    <span>TidewellOutfitters@mail.com</span>
  </div>
</section>

</body>
</html>
```